Wooden Floor Website

I'd like a Modern and crisp site with emphasis on the site being easy to navigate through - services that we offer, gallery of previous work, history, who we are, contact, etc
https://tmqrvx8219067-my.dokshelfbox.net/:b:/g/personal/marcus_bellhaven_co_uk/QWT7K2_pmRsNaHXdovtYBeLWCKjuP9e3F6kRMZbqUwnPzs

Coding

Coded - Design and coding required

Number of Pages Required

5+ page

Requirements
Must have
• Word Press Site

```html
<!DOCTYPE html>
<html lang="en">
<head>
<meta charset="utf-8">
<title>Bellhaven Flooring</title>
<link href="https://fonts.googleapis.com/css2?family=Fira+Sans:wght@400;500;600;700&family=Poppins:wght@400;500;600&display=swap" rel="stylesheet">
<style>
:root{
  --ink:#111;
  --white:#fff;
  --dark:#1f1f1f;
  --about-bg:#2a2a2a;
  --light:#e9e9e9;
  --muted:#444;
  --frame:#b88a55;
  --heading:"Fira Sans",Arial,sans-serif;
  --body:"Poppins",Arial,sans-serif;
}
*{box-sizing:border-box;margin:0;padding:0}
html,body{width:1200px;height:4018px;overflow:hidden;background:var(--white)}
body{position:relative;font-family:var(--body);color:var(--ink)}
.abs{position:absolute}
.center{left:0;width:1200px;text-align:center}

/* hero */
.hero{position:absolute;left:0;top:0;width:1200px;height:790px;
  background:linear-gradient(180deg,#7d7a74 0%,#5b5750 35%,#3b342c 70%,#4a3f33 100%)}
.hero-shade{position:absolute;inset:0;background:rgba(0,0,0,.28)}
.topbar{position:absolute;left:0;top:0;width:1200px;height:172px;background:rgba(255,255,255,.72)}
.call{left:196px;top:38px;display:flex;align-items:center;gap:12px;font-size:15px;font-weight:600}
.call small{display:block;font-size:15px;font-weight:600}
.brand-top{left:0;width:1200px;top:44px;text-align:center;font-family:var(--heading);font-weight:600;font-size:26px;letter-spacing:4px}
.search{left:762px;top:36px;width:260px;height:52px;border-radius:26px;background:var(--white);
  display:flex;align-items:center;padding:0 8px 0 26px;font-size:15px;color:#777;justify-content:space-between}
.search span.btn{width:38px;height:38px;border-radius:50%;background:var(--ink);display:flex;align-items:center;justify-content:center}
.nav{left:0;width:1200px;top:122px;display:flex;justify-content:center;gap:46px;font-size:18px;font-weight:500;text-transform:uppercase}
.nav .on{font-weight:600}
.hero-mark{left:0;width:1200px;top:350px;text-align:center;color:var(--white);font-family:var(--heading);font-weight:600;font-size:44px;letter-spacing:6px}
.hero-title{top:490px;color:var(--white);font-family:var(--heading);font-weight:600;font-size:34px}
.hero-sub{top:537px;color:var(--white);font-family:var(--heading);font-weight:600;font-size:25px}
.hero-text{left:270px;width:660px;top:576px;color:var(--white);font-size:14px;font-weight:500;line-height:32px;text-align:center;word-spacing:4px}

/* section headings */
.sec-title{font-family:var(--heading);font-weight:600;font-size:35px}
.rule{left:555px;width:90px;height:3px;background:var(--ink)}
.sec-text{left:160px;width:880px;font-size:15px;line-height:33px;text-align:center;color:var(--muted)}

/* service tiles */
.tile{position:absolute;width:341px;height:227px;display:flex;align-items:flex-end;justify-content:center;padding-bottom:14px;
  color:var(--white);font-family:var(--heading);font-weight:600;font-size:22px;text-transform:uppercase}
.t1{background:linear-gradient(180deg,#3d4a44,#6f655b)}
.t2{background:linear-gradient(180deg,#3f5a4a,#6b5c4f)}
.t3{background:linear-gradient(180deg,#cfc8bd,#5a5047)}
.t4{background:linear-gradient(180deg,#e8e6e1,#8a7864)}
.t5{background:linear-gradient(180deg,#4d4036,#3a2f27)}
.t6{background:linear-gradient(180deg,#e2e0dc,#4a4540)}
.tile::before{content:"";position:absolute;inset:0;background:linear-gradient(180deg,rgba(0,0,0,0) 55%,rgba(0,0,0,.35))}
.tile span{position:relative}

/* about */
.about{position:absolute;left:0;top:1532px;width:1200px;height:539px;background:linear-gradient(90deg,#2a2a2a,#3a3a3a 60%,#2e2e2e)}
.about-frame{left:150px;top:112px;width:425px;height:310px;background:var(--frame)}
.about-photo{left:126px;top:116px;width:437px;height:296px;background:linear-gradient(180deg,#dcdad5 0%,#c9c3b8 50%,#9d7b5b 100%)}
.about-title{left:600px;top:120px;color:var(--white);font-family:var(--heading);font-weight:600;font-size:32px}
.about-text{left:600px;top:164px;width:476px;color:var(--white);font-size:14px;line-height:26px;text-align:justify}
.btn-light{left:600px;top:367px;width:210px;height:46px;border-radius:23px;background:var(--white);
  font-family:var(--heading);font-weight:600;font-size:17px;display:flex;align-items:center;justify-content:center}

/* products */
.prod{position:absolute;width:231px;height:233px}
.prod-name{position:absolute;font-family:var(--heading);font-weight:700;font-size:21px}

/* contact */
.contact{position:absolute;left:0;top:2915px;width:1200px;height:697px;background:var(--light)}
.info{position:absolute;width:320px;text-align:center;font-size:16px;font-weight:500;line-height:26px}
.info .ico{width:86px;height:86px;border-radius:50%;background:var(--ink);margin:0 auto 22px;display:flex;align-items:center;justify-content:center}
.field{position:absolute;height:38px;background:var(--white);font-size:12px;color:#555;display:flex;align-items:center;gap:8px;padding-left:12px}
.field.area{align-items:flex-start;padding-top:12px}
.submit{position:absolute;left:512px;top:572px;width:177px;height:51px;background:var(--ink);color:var(--white);
  font-family:var(--heading);font-weight:600;font-size:17px;display:flex;align-items:center;justify-content:center;gap:10px}

/* footer */
.footer{position:absolute;left:0;top:3612px;width:1200px;height:406px;background:var(--dark);color:var(--white)}
.foot-name{top:198px;font-family:var(--heading);font-weight:600;font-size:27px;letter-spacing:2px}
.foot-links{top:250px;font-size:16px}
.foot-links i{font-style:normal;margin:0 12px}
.foot-copy{top:294px;font-size:14px;color:#ddd}
.socials{left:546px;top:344px;display:flex;gap:10px}
.socials span{width:30px;height:30px;border:2px solid var(--white);border-radius:50%}
</style>
</head>
<body>

<section class="hero" role="img" aria-label="Photo of a modern kitchen and dining room with a dark herringbone wooden floor and large garden windows">
  <div class="hero-shade"></div>
</section>

<header class="topbar">
  <div class="abs call">
    <svg width="38" height="38" viewBox="0 0 38 38"><circle cx="19" cy="19" r="17" fill="none" stroke="#111" stroke-width="2.5"/><path d="M13 11l4 0 1.5 5-2.5 2a11 11 0 0 0 5 5l2-2.5 5 1.5v4c-9 1-16-6-15-15z" fill="#111"/></svg>
    <div>Call us:<small>(555) 010-2030</small></div>
  </div>
  <div class="abs brand-top">BELLHAVEN</div>
  <div class="abs search">Search<span class="btn"><svg width="16" height="16" viewBox="0 0 16 16"><circle cx="7" cy="7" r="5" fill="none" stroke="#fff" stroke-width="2"/><path d="M11 11l4 4" stroke="#fff" stroke-width="2"/></svg></span></div>
  <nav class="abs nav">
    <span>Home</span><span>About Us</span><span>Our Services</span><span class="on">Bellhaven Flooring</span><span>Our Blog</span><span>Testimonials</span><span>Contact Us</span>
  </nav>
</header>

<div class="hero-mark">BELLHAVEN</div>
<h1 class="abs center hero-title">BELLHAVEN FLOORING</h1>
<p class="abs center hero-sub">WE PROVIDE ULTIMATE FLOORING &nbsp;AND PAVING SERVICES.</p>
<p class="abs hero-text">Sed ut perspiciatis unde omnis iste natus error sit voluptatem accusantium doloremque laudantium, totam rem aperiam, eaque ipsa quae.</p>

<section class="services">
  <h2 class="abs center sec-title" style="top:838px">WE PROVIDE FLOORING SERVICES</h2>
  <div class="abs rule" style="top:893px"></div>
  <p class="abs sec-text" style="top:904px">Sed ut perspiciatis unde omnis iste natus error sit voluptatem accusantium doloremque laudantium, totam rem aperiam, eaque ipsa quae ab illo inventore veritatis et quasi architecto beatae vitae dicta sunt explicabo.</p>
  <div class="tile t1" style="left:72px;top:999px" role="img" aria-label="Living room with brushed oak floor"><span>Brushed</span></div>
  <div class="tile t2" style="left:430px;top:999px" role="img" aria-label="Bathroom with bandsawn oak floor"><span>Bandsawn</span></div>
  <div class="tile t3" style="left:788px;top:999px" role="img" aria-label="Dining room with fumed oak floor"><span>Fumed</span></div>
  <div class="tile t4" style="left:72px;top:1243px" role="img" aria-label="Kitchen with light smoked oak floor"><span>Light Smoked</span></div>
  <div class="tile t5" style="left:430px;top:1243px" role="img" aria-label="Medium smoked herringbone floor with plant"><span>Medium Smoked</span></div>
  <div class="tile t6" style="left:788px;top:1243px" role="img" aria-label="Hallway with dark smoked oak floor"><span>Dark Smoked</span></div>
</section>

<section class="about" role="img" aria-label="Dim interior of a large glazed room with wooden floor">
  <div class="abs about-frame"></div>
  <div class="abs about-photo" role="img" aria-label="Bright kitchen with light oak plank floor and dining chairs"></div>
  <h2 class="abs about-title">ABOUT US</h2>
  <p class="abs about-text">Sed ut perspiciatis unde omnis iste natus error sit voluptatem accusantium doloremque laudantium, totam rem aperiam, eaque ipsa quae ab illo inventore veritatis et quasi architecto beatae vitae dicta sunt explicabo. Nemo enim ipsam voluptatem quia voluptas sit aspernatur aut odit aut fugit, sed quia consequuntur magni dolores eos qui ratione voluptatem sequi nesciunt.</p>
  <div class="abs btn-light">READ MORE</div>
</section>

<section class="products">
  <h2 class="abs center sec-title" style="top:2118px">JUST ARRIVED PRODUCTS</h2>
  <div class="abs rule" style="top:2173px"></div>
  <p class="abs sec-text" style="top:2184px">Sed ut perspiciatis unde omnis iste natus error sit voluptatem accusantium doloremque laudantium, totam rem aperiam, eaque ipsa quae ab illo inventore veritatis et quasi architecto beatae vitae dicta sunt explicabo.</p>

  <div class="prod" style="left:104px;top:2291px;background:#1e1e1e" role="img" aria-label="Black herringbone wood sample"></div>
  <div class="prod" style="left:358px;top:2291px;background:linear-gradient(135deg,#8a5a2e,#a8743f,#7b4f28)" role="img" aria-label="Mid brown matt herringbone wood sample"></div>
  <div class="prod" style="left:613px;top:2291px;background:linear-gradient(135deg,#9a6a3c,#b8834f,#8c5e33)" role="img" aria-label="Honey satin herringbone wood sample"></div>
  <div class="prod" style="left:866px;top:2291px;background:linear-gradient(135deg,#4a3322,#6b4a30,#3f2b1c)" role="img" aria-label="Dark brown herringbone wood sample"></div>
  <div class="prod-name" style="left:104px;top:2528px">BH904</div>
  <div class="prod-name" style="left:358px;top:2528px">BH910 - MATT</div>
  <div class="prod-name" style="left:613px;top:2528px">BH911 - SATIN</div>
  <div class="prod-name" style="left:866px;top:2528px">BH916</div>

  <div class="prod" style="left:104px;top:2594px;background:linear-gradient(135deg,#d8cdb4,#c9bb9c,#ddd3bd)" role="img" aria-label="Pale natural herringbone wood sample"></div>
  <div class="prod" style="left:358px;top:2594px;background:linear-gradient(135deg,#8f8070,#a39383,#85766a)" role="img" aria-label="Grey brown herringbone wood sample"></div>
  <div class="prod" style="left:613px;top:2594px;background:linear-gradient(135deg,#9c8f82,#b1a396,#8f8276)" role="img" aria-label="Smoky grey herringbone wood sample"></div>
  <div class="prod" style="left:866px;top:2594px;background:linear-gradient(135deg,#a09484,#b4a898,#968a7b)" role="img" aria-label="Light grey herringbone wood sample"></div>
  <div class="prod-name" style="left:104px;top:2831px">BH922</div>
  <div class="prod-name" style="left:358px;top:2831px">BH923</div>
  <div class="prod-name" style="left:613px;top:2831px">BH929</div>
  <div class="prod-name" style="left:866px;top:2831px">BH938</div>
</section>

<section class="contact">
  <h2 class="abs center sec-title" style="top:66px">CONTACT US</h2>
  <div class="info" style="left:175px;top:148px">
    <div class="ico"><svg width="40" height="44" viewBox="0 0 40 44"><path d="M20 4a11 11 0 0 1 11 11c0 8-11 19-11 19S9 23 9 15A11 11 0 0 1 20 4z" fill="none" stroke="#fff" stroke-width="2.2"/><circle cx="20" cy="15" r="4" fill="none" stroke="#fff" stroke-width="2.2"/><path d="M6 32l-3 9h34l-3-9" fill="none" stroke="#fff" stroke-width="2"/></svg></div>
    Lindenweg Str. 18, Marlbach<br>Rheinland-Pfalz - 55012
  </div>
  <div class="info" style="left:462px;top:148px">
    <div class="ico"><svg width="40" height="40" viewBox="0 0 40 40"><path d="M9 5h8l3 9-5 4a20 20 0 0 0 8 8l4-5 9 3v8C20 34 6 20 9 5z" fill="none" stroke="#fff" stroke-width="2.2"/></svg></div>
    Phone:<br>555 010 2030
  </div>
  <div class="info" style="left:754px;top:148px">
    <div class="ico"><svg width="44" height="32" viewBox="0 0 44 32"><rect x="2" y="2" width="40" height="28" fill="none" stroke="#fff" stroke-width="2.2"/><path d="M2 2l20 16L42 2M2 30l15-14M42 30L27 16" fill="none" stroke="#fff" stroke-width="2"/></svg></div>
    Email:<br>info@bellhaven-example.com
  </div>

  <form>
    <div class="field" style="left:166px;top:349px;width:424px">&#9679; First Name</div>
    <div class="field" style="left:166px;top:405px;width:424px">&#9679; Last Name</div>
    <div class="field" style="left:166px;top:459px;width:424px">&#9993; Email Address</div>
    <div class="field" style="left:166px;top:515px;width:424px">&#9742; Phone Number</div>
    <div class="field" style="left:614px;top:349px;width:423px">&#9881; Treatment</div>
    <div class="field area" style="left:614px;top:405px;width:423px;height:145px">&#9998; Message :</div>
    <div class="submit"><svg width="20" height="20" viewBox="0 0 20 20"><path d="M1 9L19 1 12 19 9 11z" fill="#fff"/></svg>SUBMIT</div>
  </form>
</section>

<footer class="footer">
  <div class="abs center" style="top:96px;font-family:var(--heading);font-weight:600;font-size:40px;letter-spacing:6px">BELLHAVEN</div>
  <div class="abs center foot-name">BELLHAVEN FLOORING</div>
  <div class="abs center foot-links">Home<i>|</i>About Us<i>|</i>Our Services<i>|</i>Blog<i>|</i>Testimonials<i>|</i>Contact Us</div>
  <div class="abs center foot-copy">© 2019 Company Name &nbsp;All right reserved</div>
  <div class="abs socials"><span></span><span></span><span></span></div>
</footer>

</body>
</html>
```